Eiskarte für Cafe - Konditorei
Sehr tolle Eiskarte geworden. Ganz nach meiner Vorstellung - Vielen Dank dafür
Aufgabenstellung
4 Seiten im A5 Hochformat - Titelseite ohne Eisbecher ob alles auf den 2 Innenseiten Platz hat oder auf der Rückseite noch etwas hinkommt müssen wir schauen - Logo vom Eis und Firmenlogo soll eingebaut werden - nicht zu schrill vielleicht

```html
<!DOCTYPE html>
<html lang="de">
<head>
<meta charset="utf-8">
<title>Eiskarte – Hain Konditorei</title>
<link href="https://fonts.googleapis.com/css2?family=Jost:wght@300;400;500&display=swap" rel="stylesheet">
<style>
:root{
  --paper:#efede6;
  --bg:#ffffff;
  --accent:#f2b349;
  --ink:#1d1b1a;
  --muted:#6e6a64;
  --faint:#cdc6bb;
  --label:#c9c3b9;
}
*{margin:0;padding:0;box-sizing:border-box}
html,body{width:1200px;height:2456px;overflow:hidden;background:var(--bg)}
body{position:relative;font-family:"Jost",sans-serif;color:var(--ink)}
.page{position:absolute;background:var(--paper);box-shadow:8px 10px 10px rgba(0,0,0,.45)}
.cover{left:580px;top:68px;width:520px;height:754px}
.spread{left:62px;top:870px;width:1035px;height:730px;box-shadow:6px 8px 10px rgba(0,0,0,.35);outline:1px solid #d8d5cc}
.back{left:580px;top:1650px;width:517px;height:754px}
.fold{position:absolute;left:518px;top:0;width:1px;height:100%;background:#cfcbc2}
.band{position:absolute;top:0;width:32px;height:100%;background:var(--accent)}
.cover .band{left:0}
.back .band{right:0}
.visual{position:absolute}
.cover .visual{left:32px;top:50px;width:180px;height:650px;background:linear-gradient(180deg,rgba(205,198,187,.45),rgba(205,198,187,.15));border-radius:90px 90px 20px 20px}
.brand{position:absolute;display:flex;align-items:center;gap:14px;color:var(--ink)}
.brand .dot{width:62px;height:62px;border:5px solid var(--ink);border-radius:50%;flex:none}
.brand .name{font-weight:500;line-height:.9}
.brand .big{font-size:74px;letter-spacing:1px;display:block}
.brand .sub{font-size:30px;display:block;letter-spacing:.5px}
.brand .place{font-size:19px;display:block;margin-top:6px;letter-spacing:.3px}
.cover .brand{left:95px;top:295px}
.cover .title{position:absolute;left:0;width:100%;padding-left:90px;top:640px;text-align:center;font-size:32px;font-weight:400;letter-spacing:2px;color:var(--label)}
.back .brand{left:103px;top:376px;gap:10px}
.back .brand .dot{width:44px;height:44px;border-width:4px}
.back .brand .big{font-size:50px}
.back .brand .sub{font-size:20px}
.back .brand .place{font-size:13px;margin-top:4px}
.address{position:absolute;left:182px;top:537px;width:155px;border-top:2px dotted var(--muted);padding-top:16px;font-size:14px;font-weight:300;line-height:1.4;letter-spacing:.5px;color:var(--muted)}
.partner{position:absolute;top:73px;width:110px;text-align:center;font-size:22px;font-weight:400;color:var(--ink);display:flex;align-items:center;justify-content:center;gap:6px}
.partner .mark{width:12px;height:12px;border-radius:50%;background:var(--ink)}
.partner.left{left:200px}
.partner.right{left:722px}
.photo-left{left:0;top:178px;width:146px;height:487px;background:linear-gradient(180deg,rgba(186,150,105,.6),rgba(220,205,170,.6) 55%,rgba(239,237,230,0));border-radius:0 50px 0 0}
.photo-right{right:0;top:173px;width:114px;height:517px;background:linear-gradient(180deg,rgba(224,110,140,.6),rgba(175,220,190,.6) 55%,rgba(239,237,230,0));border-radius:50px 0 0 0}
.menu{position:absolute;list-style:none;width:316px}
.menu.left{left:105px;top:205px}
.menu.right{left:623px;top:205px}
.item{margin-bottom:19px}
.item-head{display:flex;justify-content:space-between;font-size:12.5px;font-weight:400;letter-spacing:.3px}
.item-desc{font-size:11px;font-weight:300;line-height:1.35;color:var(--muted);margin-top:4px;max-width:275px;text-transform:uppercase}
.rule{border-top:2px dotted var(--ink);width:186px;margin:28px 0 24px}
.extras-title{font-size:15px;font-weight:400;letter-spacing:.5px;margin-bottom:12px}
.extra{display:flex;justify-content:space-between;font-size:11.5px;font-weight:300;margin-bottom:7px}
</style>
</head>
<body>

<section class="page cover">
  <div class="band"></div>
  <div class="visual" role="img" aria-label="Faint line illustration of an ice cream sundae with wafers"></div>
  <div class="brand">
    <span class="dot"></span>
    <span class="name"><span class="big">HAIN</span><span class="sub">KONDITOREI</span><span class="place">BAD LINDENAU</span></span>
  </div>
  <h1 class="title">EISKARTE</h1>
</section>

<section class="page spread">
  <div class="fold"></div>
  <div class="visual photo-left" role="img" aria-label="Photo of a coffee ice cream sundae with cone"></div>
  <div class="visual photo-right" role="img" aria-label="Photo of colourful ice cream scoops with sweets"></div>
  <div class="partner left"><span class="mark"></span>solvara eis</div>
  <div class="partner right"><span class="mark"></span>solvara eis</div>

  <ul class="menu left">
    <li class="item"><div class="item-head"><span>EISKAFFEE</span><span>6.90</span></div><p class="item-desc">Cremiges Vanilleeis, gekühlter Kaffee, Schlagobers und Schokostreusel</p></li>
    <li class="item"><div class="item-head"><span>EISSCHOKOLADE</span><span>6.90</span></div><p class="item-desc">Cremiges Vanilleeis, gekühlte Trinkschoki, Schlagobers und Schokostreusel</p></li>
    <li class="item"><div class="item-head"><span>BANANENSPLIT</span><span>7.90</span></div><p class="item-desc">Cremiges Vanille- und Schokoladeneis, frische Banane, Schokosauce, geröstete Mandelblättchen &amp; Schlagobers</p></li>
    <li class="item"><div class="item-head"><span>FRUCHTEISBECHER</span><span>8.50</span></div><p class="item-desc">Gemischtes Fruchteis, frische Früchte der Saison, Fruchtsauce und Schlagobers</p></li>
    <li class="item"><div class="item-head"><span>JOGHURTBECHER</span><span>8.50</span></div><p class="item-desc">Joghurteis, Himbeereis, Beereneis, Naturjoghurt, Beeren der Saison und Schlagobers</p></li>
    <li class="item"><div class="item-head"><span>COUPE DÄNEMARK</span><span>7.50</span></div><p class="item-desc">Cremiges Vanille- und Schokoladeneis mit Schlagobers &amp; Schokosauce</p></li>
    <li class="item"><div class="item-head"><span>ERDBEEREISCOUP</span><span>8.50</span></div><p class="item-desc">Cremiges Erdbeer- und Vanilleeis, frische Erdbeeren, Schlagobers und Erdbeersauce</p></li>
  </ul>

  <ul class="menu right">
    <li class="item"><div class="item-head"><span>NUSSBECHER</span><span>8.50</span></div><p class="item-desc">Cremiges Vanille-, Haselnuss- und Pistazieneis, Schlagobers, Sauce Karamell, gemischte Nüsse, Nusskrokant und Nuvetto</p></li>
    <li class="item"><div class="item-head"><span>AMARENA EISBECHER</span><span>7.90</span></div><p class="item-desc">Cremiges Vanille- und Schokoladeneis, Amarenakirschen, Schokosauce und Schlagobers</p></li>
    <li class="item"><div class="item-head"><span>KINDEREISBECHER</span><span>4.90</span></div><p class="item-desc">2 Kugeln Eis, mit Schlagobers und bunten Farbinis</p></li>
    <li class="item"><div class="item-head"><span>GEMISCHTES EIS IM GLAS:</span></div>
      <div class="extra" style="margin-top:6px"><span>2 KUGELN</span><span>4.40</span></div>
      <div class="extra"><span>3 KUGELN</span><span>6.50</span></div></li>
    <li><div class="rule"></div>
      <h2 class="extras-title">EXTRAS</h2>
      <div class="extra"><span>PORTION SCHLAGOBERS</span><span>1.50</span></div>
      <div class="extra"><span>WAFFELN</span><span>1.40</span></div>
      <div class="extra"><span>BELLMOOR, EIERLIKÖR UND AMARETTO</span><span>0.00</span></div></li>
  </ul>
</section>

<section class="page back">
  <div class="band"></div>
  <div class="brand">
    <span class="dot"></span>
    <span class="name"><span class="big">HAIN</span><span class="sub">KONDITOREI</span><span class="place">BAD LINDENAU</span></span>
  </div>
  <p class="address">STRASSENNAME 11<br>22222 ORTSCHAFT</p>
</section>

</body>
</html>
```